physical therapy flyer

2 office locations speciality programs - work injury / Motor vehicle accidents - spanish speaking - do not put balance defecits/ fall prevention - Spanish speaking
neck and back pain shoulder pain/ rotator cuff disorder / bursitis
hip pain knee andle and foot pain post operative care including Spine , shoulder , knee , total joint replacement

Meadowlark Physical therapy & Chiropractic
4827 Ashbury BLvd
lindell park ny 11592
7185528174
3719 Tillman Parkway
Corvale NY 11592
7182947061
www.meadowlarkptchiroacu.com

```html
<!DOCTYPE html>
<html lang="en">
<head>
<meta charset="utf-8">
<title>Meadowlark Physical Therapy Flyer</title>
<link rel="stylesheet" href="https://fonts.googleapis.com/css2?family=Poppins:wght@400;500;600;700;800&display=swap">
<style>
  :root {
    --page-bg: #8fa9aa;
    --paper: #f2f2f0;
    --green: #3aa83c;
    --green-light: #62b531;
    --green-dark: #1f8a2f;
    --green-band: #52a82c;
    --charcoal: #2a2a2a;
    --white: #ffffff;
    --photo-light: #e4e1dc;
    --photo-mid: #c9c2b8;
  }
  * { margin: 0; padding: 0; box-sizing: border-box; }
  html, body { width: 1200px; height: 1117px; overflow: hidden; }
  body {
    background: var(--page-bg);
    font-family: "Poppins", sans-serif;
    position: relative;
  }
  .flyer {
    position: absolute;
    left: 219px; top: 20px;
    width: 762px; height: 1077px;
    background: var(--paper);
    overflow: hidden;
    box-shadow: 0 6px 24px rgba(0,0,0,0.25);
  }
  .hero-photo {
    position: absolute; left: 0; top: 0;
    width: 762px; height: 281px;
    background: linear-gradient(100deg, var(--photo-mid) 0%, var(--photo-light) 35%, #eeebe6 70%, #e9e6e1 100%);
  }
  .programs {
    position: absolute; left: 370px; top: 30px;
    width: 363px; height: 501px;
    background: var(--green);
    border-radius: 20px 20px 48px 20px;
    color: var(--white);
  }
  .programs .count {
    position: absolute; left: 32px; top: 14px;
    font-size: 68px; font-weight: 700; line-height: 1;
  }
  .programs .title {
    position: absolute; left: 88px; top: 38px;
    font-size: 18.5px; font-weight: 700; line-height: 1.15;
    text-transform: uppercase;
  }
  .program-list { list-style: none; }
  .program-list li {
    position: absolute; left: 68px; width: 285px;
    font-size: 17.2px; font-weight: 400; line-height: 1.16;
  }
  .program-list li svg {
    position: absolute; left: -28px; top: 4px;
    width: 14px; height: 12px;
  }
  .brand {
    position: absolute; left: 53px; top: 308px;
    display: flex; align-items: center; gap: 10px;
  }
  .brand .dot {
    width: 38px; height: 38px; border-radius: 50%;
    background: var(--green-dark);
  }
  .brand .name {
    font-size: 15.5px; font-weight: 400; line-height: 1.2;
    color: var(--green-dark);
  }
  .headline {
    position: absolute; left: 40px; top: 394px; width: 320px;
    text-align: center;
    font-weight: 800; line-height: 0.98; font-size: 47px;
    text-transform: uppercase;
  }
  .headline .light { display: block; color: var(--green-light); letter-spacing: -0.5px; }
  .headline .dark { display: block; color: var(--green-dark); }
  .gallery .photo {
    position: absolute; top: 561px;
    width: 223px; height: 205px;
    border-radius: 14px;
    box-shadow: 0 8px 0 -2px #d9d9d6;
  }
  .photo-neck { left: 40px; background: linear-gradient(135deg, #d9d6d1, #b8a89a 60%, #e6e3de); }
  .photo-arm { left: 270px; background: linear-gradient(135deg, #c9a48c, #e7e2dc 50%, #2e3a55); }
  .photo-back { left: 499px; background: linear-gradient(135deg, #8e9aa6, #3f5b7a 55%, #c8ccd0); }
  .footer-shape { position: absolute; left: 0; top: 760px; width: 762px; height: 317px; }
  .clinic-name {
    position: absolute; left: 78px; top: 812px;
    width: 608px; height: 45px;
    background: rgba(40,120,30,0.35);
    border-radius: 8px;
    color: var(--white);
    font-size: 22px; font-weight: 600;
    text-align: center; line-height: 45px;
  }
  .location {
    position: absolute; top: 877px;
    color: var(--white);
    font-size: 19.5px; font-weight: 500; line-height: 1.2;
  }
  .location-west { left: 92px; }
  .location-east { left: 423px; }
  .location .line { display: flex; gap: 6px; }
  .location .line svg { flex: none; width: 14px; height: 18px; margin-top: 3px; }
  .location .phone { margin-top: 13px; }
  .divider {
    position: absolute; left: 380px; top: 873px;
    width: 1px; height: 89px;
    background: rgba(255,255,255,0.35);
  }
  .website {
    position: absolute; left: 0; top: 1020px; width: 762px;
    text-align: center;
    color: var(--white);
    font-size: 22px; font-weight: 700;
  }
</style>
</head>
<body>
  <main class="flyer">
    <div class="hero-photo" role="img" aria-label="Photo of a physical therapist explaining a spine model to a patient"></div>

    <section class="programs">
      <div class="count">2</div>
      <h2 class="title">Office locations<br>speciality programs</h2>
      <ul class="program-list">
        <li style="top:114px"><svg viewBox="0 0 14 12"><path d="M1 6.5 5 10 13 1.5" fill="none" stroke="#fff" stroke-width="2.6"/></svg>work injury / Motor vehicle accidents -</li>
        <li style="top:175px"><svg viewBox="0 0 14 12"><path d="M1 6.5 5 10 13 1.5" fill="none" stroke="#fff" stroke-width="2.6"/></svg>do not put balance defecits/ fall prevention</li>
        <li style="top:236px"><svg viewBox="0 0 14 12"><path d="M1 6.5 5 10 13 1.5" fill="none" stroke="#fff" stroke-width="2.6"/></svg>neck and back pain</li>
        <li style="top:277px"><svg viewBox="0 0 14 12"><path d="M1 6.5 5 10 13 1.5" fill="none" stroke="#fff" stroke-width="2.6"/></svg>shoulder pain / rotator cuff</li>
        <li style="top:318px"><svg viewBox="0 0 14 12"><path d="M1 6.5 5 10 13 1.5" fill="none" stroke="#fff" stroke-width="2.6"/></svg>disorder / bursitis</li>
        <li style="top:359px"><svg viewBox="0 0 14 12"><path d="M1 6.5 5 10 13 1.5" fill="none" stroke="#fff" stroke-width="2.6"/></svg>hip pain knee andle and foot pain post operative care including Spine , shoulder , knee , total joint replacement</li>
        <li style="top:460px"><svg viewBox="0 0 14 12"><path d="M1 6.5 5 10 13 1.5" fill="none" stroke="#fff" stroke-width="2.6"/></svg>spanish speaking</li>
      </ul>
    </section>

    <div class="brand">
      <span class="dot"></span>
      <span class="name">Meadowlark Physical Therapy,<br>Chiropractic, and Acupuncture</span>
    </div>

    <h1 class="headline">
      <span class="light">We create</span>
      <span class="dark">Healthy</span>
      <span class="dark">Families</span>
    </h1>

    <div class="gallery">
      <div class="photo photo-neck" role="img" aria-label="Photo of a therapist stretching a patient's neck"></div>
      <div class="photo photo-arm" role="img" aria-label="Photo of a therapist working on a patient's arm"></div>
      <div class="photo photo-back" role="img" aria-label="Photo of a therapist assisting an older man with back pain"></div>
    </div>

    <svg class="footer-shape" viewBox="0 0 762 317" preserveAspectRatio="none" aria-hidden="true">
      <path d="M0 58 Q381 -10 762 58 L762 317 L0 317 Z" fill="var(--green-band)"/>
      <path d="M0 258 Q381 210 762 258 L762 317 L0 317 Z" fill="#4a9d26"/>
      <path d="M0 276 Q381 226 762 276 L762 317 L0 317 Z" fill="var(--charcoal)"/>
    </svg>

    <div class="clinic-name">Meadowlark Physical therapy &amp; Chiropractic</div>

    <div class="location location-west">
      <div class="line"><svg viewBox="0 0 14 18"><path d="M7 0C3 0 0 3 0 7c0 5 7 11 7 11s7-6 7-11c0-4-3-7-7-7zm0 10a3 3 0 1 1 0-6 3 3 0 0 1 0 6z" fill="#fff"/></svg><span>4827 Ashbury BLvd<br>lindell park ny 11592</span></div>
      <div class="line phone"><svg viewBox="0 0 16 16"><circle cx="8" cy="8" r="8" fill="#fff"/><path d="M5 4l2 2-1 1.2c.6 1.2 1.6 2.2 2.8 2.8L10 9l2 2-1.4 1.4C7.5 12 4 8.5 3.6 5.4z" fill="var(--green-band)"/></svg><span>7185528174</span></div>
    </div>
    <div class="divider"></div>
    <div class="location location-east">
      <div class="line"><svg viewBox="0 0 14 18"><path d="M7 0C3 0 0 3 0 7c0 5 7 11 7 11s7-6 7-11c0-4-3-7-7-7zm0 10a3 3 0 1 1 0-6 3 3 0 0 1 0 6z" fill="#fff"/></svg><span>3719 Tillman Parkway<br>Corvale NY 11592</span></div>
      <div class="line phone"><svg viewBox="0 0 16 16"><circle cx="8" cy="8" r="8" fill="#fff"/><path d="M5 4l2 2-1 1.2c.6 1.2 1.6 2.2 2.8 2.8L10 9l2 2-1.4 1.4C7.5 12 4 8.5 3.6 5.4z" fill="var(--green-band)"/></svg><span>7182947061</span></div>
    </div>

    <div class="website">www.meadowlarkptchiroacu.com</div>
  </main>
</body>
</html>
```